Tending Our Garden eBook Cover Design

I want to deisgn a cover for my eBook (FRONT COVER) and the title is:

What I Grew From a Single Spark. And Why It Matters
By KT Dorran

TITLE CHANGED TO: UNDER THE WILLOW TREE; WHERE I FOUND MY QUIET STRENGTH AND WHERE YOU MIGHT TOO

The color palette is attached. Along with some photos options of me. Along with the ebook in WORD Document. My website is www.KTDorranLive.example. You can use a different color palette if you think it is best

Target Market(s)

women who look to build a personal brand

Industry/Entity Type

health and wellness

Requirements
Must have
• the title
Nice to have
• use my picture on the cover; but that is optional
Should not have
• any men

```html
<!DOCTYPE html>
<html lang="en">
<head>
<meta charset="utf-8">
<title>Under the Willow Tree — KT Dorran</title>
<link href="https://fonts.googleapis.com/css2?family=Bebas+Neue&family=Montserrat:wght@700;800&family=Great+Vibes&display=swap" rel="stylesheet">
<style>
  :root {
    --backdrop: #5b5b5b;
    --blush: #f4cbbb;
    --blush-light: #fdf1ec;
    --wine-top: #5c2830;
    --wine-bottom: #460707;
    --wine-ink: #4a1a1c;
    --white: #ffffff;
    --rose-text: #f3d2c6;
    --rose-soft: #f7e0d8;
  }
  * { margin: 0; padding: 0; box-sizing: border-box; }
  html, body { width: 851px; height: 1200px; overflow: hidden; background: var(--backdrop); }
  .cover {
    position: absolute; left: 120px; top: 111px; width: 611px; height: 977px;
    overflow: hidden;
    background: radial-gradient(ellipse at 50% 55%, var(--blush-light) 0%, var(--blush) 75%);
    box-shadow: 0 12px 30px rgba(0,0,0,.35);
  }
  .center-band {
    position: absolute; left: 74px; top: 0; width: 464px; height: 100%;
    background: linear-gradient(180deg, var(--wine-top) 0%, #561820 55%, var(--wine-bottom) 100%);
  }
  .title-tag {
    position: absolute; left: 138px; top: 68px; width: 336px; height: 52px;
    background: var(--blush); transform: rotate(-2deg);
    box-shadow: 0 3px 6px rgba(0,0,0,.35);
    display: flex; align-items: center; justify-content: center;
    font: 800 19px/1 'Montserrat', sans-serif; color: var(--wine-ink); letter-spacing: .3px;
  }
  .title-line {
    position: absolute; left: 0; width: 611px; top: 140px; text-align: center;
    font: 400 54px/1 'Bebas Neue', sans-serif; color: var(--white); letter-spacing: 1px;
  }
  .title-hero {
    position: absolute; left: 0; width: 611px; top: 214px; text-align: center;
    font: 400 150px/1 'Bebas Neue', sans-serif; color: var(--white);
    -webkit-text-stroke: 18px var(--wine-ink); paint-order: stroke fill;
    text-shadow: 0 6px 10px rgba(0,0,0,.25);
  }
  .author-photo {
    position: absolute; left: 16px; top: 392px; width: 310px; height: 585px;
    border-radius: 110px 110px 0 0;
    background: linear-gradient(180deg, #3a2a2a 0%, #1c1a1c 45%, #141214 100%);
  }
  .subtitle {
    position: absolute; right: 99px; top: 425px; text-align: right;
    font-family: 'Montserrat', sans-serif; color: var(--white);
  }
  .subtitle .lead { display: block; font-weight: 700; font-size: 17px; line-height: 24px; }
  .subtitle .big { display: block; font-weight: 800; font-size: 44px; line-height: 50px; }
  .subtitle .rose { color: var(--rose-text); }
  .subtitle .soft { color: var(--rose-soft); }
  .byline {
    position: absolute; right: 99px; top: 752px;
    font: 400 76px/1 'Great Vibes', cursive; color: var(--white);
  }
  .author-name {
    position: absolute; right: 99px; top: 862px;
    font: 800 32px/1 'Montserrat', sans-serif; color: var(--rose-text); letter-spacing: .5px;
  }
</style>
</head>
<body>
  <main class="cover">
    <div class="center-band"></div>
    <div class="title-tag">UNDER THE WILLOW TREE;</div>
    <h1 class="title-line">WHERE I FOUND MY QUIET</h1>
    <div class="title-hero">STRENGTH</div>
    <div class="author-photo" role="img" aria-label="Portrait of the author in a black outfit, smiling and waving"></div>
    <p class="subtitle">
      <span class="lead">And Where</span>
      <span class="big">YOU</span>
      <span class="big rose">MIGHT</span>
      <span class="big soft">TOO</span>
    </p>
    <div class="byline">By</div>
    <div class="author-name">KT DORRAN</div>
  </main>
</body>
</html>
```